Want to fly? Flight school needs a roll up

Hello designers

We are a small aviation club with around 100 members. We love flying and therefore offer free flight lessons for young people at our glider flight school.
The young people only have to pay a flat rate of €300 for the aircraft until their first solo flight.
To advertise the flight school we now need a roll up banner measuring 85cm x 200cm. You can find the data sheet for the banner in the appendix.
Content of the roll up banner:
Advertising for our flight school so that we can attract new members
The banner should be designed in our club colors blue/white
The banner is aimed at all people who want to get a glider license
A great offer for young people up to the age of 25 should be placed on the banner with a reference to the text “Offer only applies to people up to the age of 25. Included in the flat rate of €300 is training on the glider up to the first "solo flight"
The banner is intended to advertise training with a glider. Therefore the wish would be for a glider to be depicted

Here is a link to our current homepage

https://www.lsg-kornbach.de/

https://www.videohub-example.com/watch?v=Q8-t2Lp4xZn

Target Market(s)

Young people from 14 years to 30 years

Colors
0054AA
0677BA
7BADD7
CADEEF
E8F1F8

Requirements
Nice to have
• Glider / club logo
Should not have
• Too much text

```html
<!DOCTYPE html>
<html lang="en">
<head>
<meta charset="utf-8">
<title>Glider Flight School Roll-up</title>
<link href="https://fonts.googleapis.com/css2?family=Oswald:wght@500;600;700&family=Poppins:ital,wght@0,600;0,800;1,800&display=swap" rel="stylesheet">
<style>
  :root {
    --navy: #10129a;
    --royal: #1d22c4;
    --periwinkle: #a9acf7;
    --sky-deep: #5f86d8;
    --sky: #9cc0ec;
    --sky-pale: #cadeef;
    --ink: #05061a;
    --night: #0d0f3a;
    --red: #e41e1e;
    --white: #ffffff;
    --page: #f4f5f7;
  }
  html, body {
    margin: 0;
    padding: 0;
    width: 1200px;
    height: 4000px;
    overflow: hidden;
    background: var(--page);
  }
  .rollup {
    position: absolute;
    left: 0;
    top: 588px;
    width: 1200px;
    height: 2824px;
    overflow: hidden;
    box-shadow: 0 10px 30px rgba(0,0,0,.25);
  }
  .rollup__art {
    position: absolute;
    inset: 0;
  }
  .text {
    position: absolute;
    margin: 0;
    white-space: nowrap;
    line-height: 1;
  }
  .club-name {
    position: absolute;
    left: 94px;
    top: 42px;
    width: 410px;
    height: 410px;
    display: flex;
    align-items: center;
    justify-content: center;
    text-align: center;
    font-family: "Poppins", sans-serif;
    font-weight: 800;
    font-size: 44px;
    line-height: 1.15;
    color: var(--navy);
  }
  .headline {
    font-family: "Oswald", sans-serif;
    font-weight: 700;
    color: var(--white);
    left: 96px;
  }
  .headline--free { top: 545px; font-size: 152px; }
  .headline--flight { top: 700px; font-size: 190px; color: var(--periwinkle); }
  .headline--lessons { top: 888px; font-size: 138px; }
  .offer-note {
    left: 100px;
    top: 1046px;
    font-family: "Poppins", sans-serif;
    font-weight: 600;
    font-size: 54px;
    line-height: 1;
    color: var(--white);
  }
  .age-label {
    left: 205px;
    top: 1194px;
    font-family: "Poppins", sans-serif;
    font-style: italic;
    font-weight: 800;
    font-size: 86px;
    color: var(--navy);
  }
  .training-lead {
    left: 96px;
    top: 1722px;
    font-family: "Oswald", sans-serif;
    font-weight: 500;
    font-size: 72px;
    color: var(--ink);
    transform: scaleX(.86);
    transform-origin: left;
  }
  .training-goal {
    left: 92px;
    top: 1800px;
    font-family: "Poppins", sans-serif;
    font-weight: 800;
    font-size: 102px;
    color: var(--ink);
  }
  .flat-rate {
    left: 158px;
    top: 1966px;
    font-family: "Poppins", sans-serif;
    font-style: italic;
    font-weight: 800;
    font-size: 70px;
    line-height: 72px;
    color: var(--white);
  }
  .price {
    left: 768px;
    top: 2006px;
    width: 290px;
    text-align: center;
    font-family: "Oswald", sans-serif;
    font-weight: 600;
    font-size: 100px;
    color: var(--white);
  }
  .website {
    left: 0;
    width: 1200px;
    top: 2626px;
    text-align: center;
    font-family: "Oswald", sans-serif;
    font-weight: 600;
    font-size: 120px;
    color: var(--white);
  }
</style>
</head>
<body>
<main class="rollup">
  <svg class="rollup__art" width="1200" height="2824" viewBox="0 0 1200 2824">
    <defs>
      <linearGradient id="skyFill" x1="0" y1="0" x2="0" y2="1">
        <stop offset="0" stop-color="#6f84c9"/>
        <stop offset="1" stop-color="#bcd4f2"/>
      </linearGradient>
      <linearGradient id="topSkyFill" x1="0" y1="0" x2="1" y2="1">
        <stop offset="0" stop-color="#4c5fb8"/>
        <stop offset="1" stop-color="#8fa3d9"/>
      </linearGradient>
      <linearGradient id="fieldFill" x1="0" y1="0" x2="0" y2="1">
        <stop offset="0" stop-color="#8ea58a"/>
        <stop offset=".5" stop-color="#5a6fb4"/>
        <stop offset="1" stop-color="#2a2f86"/>
      </linearGradient>
      <linearGradient id="footFill" x1="0" y1="0" x2="0" y2="1">
        <stop offset="0" stop-color="#1a1d5e" stop-opacity="0"/>
        <stop offset=".45" stop-color="#0d0f3a"/>
        <stop offset="1" stop-color="#070820"/>
      </linearGradient>
      <linearGradient id="cockpitFill" x1="0" y1="0" x2="1" y2="1">
        <stop offset="0" stop-color="#7c8fa6"/>
        <stop offset="1" stop-color="#e7ebf1"/>
      </linearGradient>
      <linearGradient id="glideFill" x1="0" y1="0" x2="0" y2="1">
        <stop offset="0" stop-color="#b7cbe9"/>
        <stop offset="1" stop-color="#d8e5f4"/>
      </linearGradient>
    </defs>

    <rect class="sky" width="1200" height="2824" fill="url(#skyFill)"/>
    <rect class="photo photo--glider-sky" x="480" y="0" width="720" height="520" fill="url(#topSkyFill)" role="img" aria-label="Photo of a white glider flying across a cloudy blue sky"/>

    <polygon class="panel panel--light" points="0,0 130,0 0,90" fill="var(--royal)"/>
    <polygon class="panel panel--dark" points="0,120 200,0 780,0 1000,150 1200,260 1200,1180 0,1640" fill="var(--navy)"/>
    <polygon class="panel panel--stripe" points="0,1520 1200,1080 1200,1180 0,1640" fill="var(--royal)"/>
    <polygon class="panel panel--stripe-top" points="360,0 520,0 1200,480 1200,540" fill="var(--royal)" opacity=".7"/>

    <rect class="photo photo--glider-low" x="0" y="1440" width="1200" height="300" fill="url(#glideFill)" role="img" aria-label="Photo of a glider flying low over the airfield"/>
    <polygon class="panel panel--stripe-mid" points="0,1480 560,1260 1200,1180 1200,1230 0,1680" fill="var(--royal)" opacity=".55"/>
    <rect class="band band--light" x="0" y="1700" width="1200" height="230" fill="var(--sky-pale)" opacity=".65"/>

    <rect class="photo photo--airfield" x="0" y="1930" width="1200" height="800" fill="url(#fieldFill)" role="img" aria-label="Photo of a red and white powered aircraft parked on the grass airfield"/>
    <rect class="footer" x="0" y="2450" width="1200" height="374" fill="url(#footFill)"/>

    <polygon class="age-band" points="104,1184 780,1184 780,1310 150,1310" fill="var(--white)"/>

    <circle cx="975" cy="698" r="240" fill="var(--white)"/>
    <circle class="photo photo--crew" cx="975" cy="698" r="228" fill="url(#cockpitFill)" role="img" aria-label="Photo of an instructor and student seated in a two-seat glider cockpit"/>
    <circle cx="980" cy="1195" r="254" fill="var(--navy)"/>
    <circle class="photo photo--student" cx="980" cy="1195" r="242" fill="url(#cockpitFill)" role="img" aria-label="Photo of a young pilot in a glider cockpit with helpers beside the canopy"/>

    <circle class="logo-disc" cx="299" cy="247" r="205" fill="var(--white)"/>

    <polygon class="price-band" points="68,1928 1012,1928 1012,2180 104,2180" fill="var(--ink)"/>
    <circle class="price-burst" cx="913" cy="2066" r="134" fill="var(--red)"/>
    <circle class="price-burst__teeth" cx="913" cy="2066" r="142" fill="none" stroke="var(--red)" stroke-width="18" stroke-dasharray="11 11"/>
  </svg>

  <div class="club-name">Luftsportgruppe<br>Kornbach e.V.</div>

  <h1 class="text headline headline--free">FREE</h1>
  <p class="text headline headline--flight">FLIGHT</p>
  <p class="text headline headline--lessons">LESSONS</p>
  <p class="text offer-note">OFFER ONLY APPLIES<br>TO PEOPLE UP&nbsp; TO THE</p>
  <p class="text age-label">AGE OF 25</p>

  <p class="text training-lead">IS TRAINING ON THE GLIDER UP TO THE</p>
  <p class="text training-goal">FIRST SOLO FLIGHT</p>
  <p class="text flat-rate">INCLUDED IN THE<br>FLAT RATE OF</p>
  <p class="text price">€300</p>

  <p class="text website">www.lsg-kornbach.de</p>
</main>
</body>
</html>
```